Web Page Design for a Website that Provides Tutoring

I am looking to create an online tutoring website. The website will allow parents or students to contact tutors with a view to instructing them to tutor themselves or their children.

The name of the website is LendYourLessons.

This brief is to create the design for one of the web pages for this web site. I am hoping the same designer will be available to design other pages.

The page I want designed is one of the more complex and I have attached the design as an excel spreadsheet. The web page needs to include all the items on this page but if you want to change the positioning of the items then Im fine with that.

I recently had two logos created for this website. My favourite is the one with a mortar board but im not sure I like the colours. I have attached both of these logos and you can use either of them, change the colours or create something different. I just want a design pleasing to the eye. If the logo is changed I would like that in a seperate file.

So can you please submit designs for this page. I have attached the two logos which you can use, change or if you feel you have a better idea then you can use that.

On the spreadsheet the Send Message, Favourite etc are buttons.

Target Market(s)

People who want to better themselves.
Possible middle class to upper class.

Industry/Entity Type

Tutoring

Number of Pages Required

1 page

Requirements
Must have
• The designs must have alot of the information attached in the spreadsheet.

```html
<!DOCTYPE html>
<html lang="en">
<head>
<meta charset="utf-8">
<title>LendYourLessons – Tutor Profile</title>
<link rel="stylesheet" href="https://fonts.googleapis.com/css2?family=Open+Sans:ital,wght@0,400;0,600;0,700;1,400&display=swap">
<style>
:root{
  --coral:#f47b5c;
  --coral-tint:#fde3db;
  --dark:#353530;
  --ink:#2f2f2f;
  --muted:#777;
  --rule:#dcdcdc;
  --grey-bg:#efeff1;
  --cell:#f2efe9;
  --amber:#f7a600;
  --olive:#9c9a36;
  --blue:#1ea3d8;
  --olive-star:#6f7a2a;
}
*{box-sizing:border-box;margin:0;padding:0}
html,body{width:1200px;height:2647px;overflow:hidden}
body{font-family:"Open Sans",Arial,sans-serif;color:var(--ink);background:#fff;position:relative}
.abs{position:absolute}
svg.star{width:18px;height:18px;display:inline-block;vertical-align:middle;margin-right:2px}

/* header */
.site-header{left:0;top:0;width:1200px;height:221px;background:var(--dark)}
.brand{left:0;width:1200px;top:52px;text-align:center;font-size:42px;font-weight:600;color:#fff;letter-spacing:-.5px}
.main-nav{left:0;width:1200px;top:146px;display:flex;justify-content:center;gap:42px;font-size:15px;color:#bdbdb8;letter-spacing:.5px}
.main-nav .active{color:var(--coral);position:relative}
.main-nav .active::after{content:"";position:absolute;left:0;right:0;bottom:-8px;height:2px;background:var(--coral)}

/* profile */
.photo{left:95px;top:270px;width:198px;height:192px;background:linear-gradient(160deg,#d9c9bd,#8a6a58 60%,#e6e2dd);border:5px solid #fff;box-shadow:0 0 0 1px #ddd}
.profile-rule-v{left:293px;top:270px;width:1px;height:192px;background:var(--rule)}
.tutor-name{left:328px;top:266px;font-size:31px;font-weight:600}
.tutor-name .first{color:var(--coral)}
.tutor-name small{font-size:12px;font-style:italic;font-weight:400;color:#999;margin-left:14px}
.actions{left:948px;top:273px;display:flex;gap:31px}
.action-btn{width:34px;height:30px;background:var(--coral);border-radius:4px;display:flex;align-items:center;justify-content:center}
.profile-rule{left:328px;top:334px;width:779px;height:1px;background:var(--rule)}
.rating{top:360px;width:200px;text-align:center}
.rating .label{font-size:18px;color:#333}
.rating .stars{margin-top:8px;height:20px}
.rating .score{margin-top:6px;font-size:22px;font-weight:700}
.facts{left:95px;top:506px;font-size:12px;font-weight:700;line-height:1}
.facts li{list-style:none;height:35px;display:flex;align-items:center;gap:8px}
.tag{background:var(--coral);color:#fff;font-weight:400;font-size:11px;padding:2px 6px;border-radius:2px;letter-spacing:.3px}
.check-badge{left:95px;top:653px;width:70px;height:50px;border:2px solid var(--coral);background:var(--coral-tint)}
.bio{left:402px;top:500px;width:705px;font-size:14.5px;line-height:35px;color:#666;text-align:justify}

/* section basics */
.band-grey{left:0;width:1200px;background:var(--grey-bg)}
.section-title{font-size:30px;font-weight:700;color:var(--ink)}
.section-title .hl{color:var(--coral)}
.rule{height:1px;background:var(--rule)}

/* subjects table */
.subjects{left:108px;top:925px;width:984px;table-layout:fixed;border-collapse:separate;border-spacing:2px 0}
.subjects th{background:var(--coral);color:#fff;font-weight:600;font-size:16px;height:44px;width:136px}
.subjects th.subject-col{width:164px}
.subjects td{background:#fff;height:60px;text-align:center;font-size:20px;font-weight:700}
.subjects tr.first td{padding-top:30px;height:90px}
.subjects tr.last td{height:110px;vertical-align:top;padding-top:14px}
.subj{display:inline-flex;align-items:center;gap:12px;width:156px;height:42px;border-radius:3px;color:#fff;font-size:16px;font-weight:700;padding-left:16px;text-align:left}
.chem{background:var(--amber)}
.bio-s{background:var(--olive)}
.price-chem{color:var(--amber)}
.price-bio{color:var(--olive)}

/* calendar */
.month-nav{left:278px;top:1384px;width:220px;display:flex;align-items:center;justify-content:space-between}
.month{font-size:22px;font-weight:600;color:var(--coral);letter-spacing:3px}
.month-arrow{width:0;height:0;border-top:7px solid transparent;border-bottom:7px solid transparent}
.weekdays{left:136px;top:1434px;width:503px;display:grid;grid-template-columns:repeat(7,1fr);font-size:16px;color:#555;text-align:center}
.calendar{left:136px;top:1473px;width:503px;border-top:5px solid var(--coral);display:grid;grid-template-columns:repeat(7,1fr);gap:1px;background:#d8d4cc}
.calendar div{height:71px;background:var(--cell);color:var(--coral);font-size:14px;padding:6px 14px}
.calendar .taken{background:var(--coral);color:#fff}
.calendar .reserved{background:var(--amber);color:#fff}
.calendar .holiday{background:var(--olive);color:#fff}
.calendar .na{background:var(--blue);color:#fff}
.legend{left:136px;top:1880px;display:flex;gap:26px;font-size:14px;color:#333;letter-spacing:.3px}
.legend span::before{content:"";display:inline-block;width:9px;height:9px;margin-right:9px;background:var(--c)}
.btn{left:750px;width:282px;height:55px;border-radius:3px;font-size:17px;display:flex;align-items:center;justify-content:center}
.btn-primary{top:1554px;background:var(--coral);color:#fff}
.btn-outline{top:1696px;border:1.5px solid var(--coral);color:var(--coral);background:#fff}
.or{left:750px;width:282px;top:1638px;text-align:center;color:#999;font-size:17px}

/* reviews */
.review-summary{left:104px;top:2091px;font-size:14px;font-style:italic;color:#555}
.review{left:127px;width:399px;height:168px;background:#fff;box-shadow:0 1px 4px rgba(0,0,0,.12);padding:16px 20px 0 85px}
.review::after{content:"";position:absolute;left:40px;bottom:-22px;border-right:34px solid transparent;border-top:22px solid #fff;filter:drop-shadow(0 2px 1px rgba(0,0,0,.08))}
.review .avatar{position:absolute;left:14px;top:18px;width:52px;height:44px;background:#f8c5b6;border-radius:4px}
.review h3{font-size:19px;font-weight:600;display:flex;align-items:center;gap:14px}
.review h3 .first{color:var(--coral)}
.review p{margin-top:10px;font-size:13.5px;line-height:21px;color:#666}
.review time{position:absolute;right:18px;bottom:12px;font-size:15px;color:#999}
.video{left:612px;top:2155px;width:484px;height:311px;background:#c9c9c9;padding:8px}
.video .screen{width:100%;height:100%;background:var(--dark);position:relative}
.video .screen .name{position:absolute;right:20px;top:232px;color:#fff;font-size:18px;font-weight:600}
.video .bar{position:absolute;left:18px;right:18px;bottom:34px;height:2px;background:#888}
.video .controls{position:absolute;left:18px;right:18px;bottom:10px;height:14px}

.site-footer{left:0;top:2626px;width:1200px;height:21px;background:var(--dark);color:#aaa;font-size:9.5px;text-align:center;line-height:21px}
</style>
</head>
<body>
<svg width="0" height="0" style="position:absolute">
  <defs>
    <symbol id="star" viewBox="0 0 20 20"><path d="M10 1l2.7 5.9 6.3.7-4.7 4.3 1.3 6.3L10 15l-5.6 3.2 1.3-6.3L1 7.6l6.3-.7z" fill="currentColor"/></symbol>
    <symbol id="star-half" viewBox="0 0 20 20"><path d="M10 1l2.7 5.9 6.3.7-4.7 4.3 1.3 6.3L10 15l-5.6 3.2 1.3-6.3L1 7.6l6.3-.7z" fill="#ccc"/><path d="M10 1v14l-5.6 3.2 1.3-6.3L1 7.6l6.3-.7z" fill="currentColor"/></symbol>
  </defs>
</svg>

<header class="site-header abs">
  <div class="brand abs">LendYourLessons</div>
  <nav class="main-nav abs">
    <span>HOME</span><span class="active">SEARCH</span><span>STUDENT</span><span>TUTOR</span><span>ABOUT</span><span>CONTACT</span><span>SIGN IN</span><span>REGISTER</span>
  </nav>
</header>

<!-- profile -->
<div class="photo abs" role="img" aria-label="Portrait photo of the tutor"></div>
<div class="profile-rule-v abs"></div>
<h1 class="tutor-name abs"><span class="first">Jane</span> Doe <small>active 15 minutes ago</small></h1>
<div class="actions abs">
  <div class="action-btn" aria-label="Send message"><svg width="18" height="14" viewBox="0 0 18 14"><rect x="1" y="1" width="16" height="12" fill="none" stroke="#fff" stroke-width="1.6"/><path d="M1 1l8 6 8-6" fill="none" stroke="#fff" stroke-width="1.6"/></svg></div>
  <div class="action-btn" aria-label="Favourite"><svg width="18" height="18" style="color:#fff"><use href="#star"/></svg></div>
  <div class="action-btn" aria-label="Chat"><svg width="18" height="16" viewBox="0 0 18 16"><ellipse cx="9" cy="7" rx="8" ry="6" fill="#fff"/><path d="M4 11l-1 4 5-3z" fill="#fff"/></svg></div>
</div>
<div class="profile-rule abs"></div>

<div class="rating abs" style="left:391px">
  <div class="label">Review Score</div>
  <div class="stars" style="color:#f68b1f"><svg class="star"><use href="#star"/></svg><svg class="star"><use href="#star"/></svg><svg class="star"><use href="#star"/></svg><svg class="star"><use href="#star"/></svg><svg class="star"><use href="#star-half"/></svg></div>
  <div class="score" style="color:#f68b1f">4.5/5</div>
</div>
<div class="rating abs" style="left:613px">
  <div class="label">Reliability</div>
  <div class="stars" style="color:var(--olive-star)"><svg class="star"><use href="#star"/></svg><svg class="star"><use href="#star"/></svg><svg class="star"><use href="#star"/></svg><svg class="star"><use href="#star"/></svg><svg class="star" style="color:#ccc"><use href="#star"/></svg></div>
  <div class="score" style="color:var(--olive)">4.0/5</div>
</div>
<div class="rating abs" style="left:816px">
  <div class="label">Punctuality</div>
  <div class="stars" style="color:var(--blue)"><svg class="star"><use href="#star"/></svg><svg class="star"><use href="#star"/></svg><svg class="star"><use href="#star"/></svg><svg class="star"><use href="#star"/></svg><svg class="star"><use href="#star-half"/></svg></div>
  <div class="score" style="color:var(--blue)">4.6/5</div>
</div>

<ul class="facts abs">
  <li>TUTORING TYPE: <span class="tag">PERSONAL</span></li>
  <li>WILLING TO TRAVEL: <span class="tag">HOME ONLY</span></li>
  <li>AGE: <span class="tag">20 YEARS OLD</span></li>
  <li>MEMBER SINCE: <span class="tag">DECEMBER 2013</span></li>
</ul>
<div class="check-badge abs" role="img" aria-label="Background check certificate badge"></div>
<p class="bio abs">Lorem ipsum dolor sit amet, consectetur adipiscing elit, sed do eiusmod tempor incididunt ut labore et dolore magna aliqua. Ut enim ad minim veniam, quis nostrud exercitation ullamco laboris nisi ut aliquip ex ea commodo consequat. Duis aute irure dolor in reprehenderit in voluptate velit esse cillum dolore eu fugiat nulla pariatur. Excepteur sint occaecat cupidatat non proident, sunt in culpa qui officia deserunt mollit anim id est laborum.Ut enim ad minim veniam, quis nostrud exercitation ullamco laboris nisi ut aliquip ex ea commodo consequat. Duis aute irure dolor in reprehenderit in voluptate velit esse cillum dolore eu fugiat nulla pariatur.</p>

<!-- subjects -->
<section class="band-grey abs" style="top:773px;height:480px">
  <h2 class="section-title abs" style="left:108px;top:40px"><span class="hl">Subjects</span> Taught</h2>
  <div class="rule abs" style="left:108px;top:109px;width:984px"></div>
</section>
<table class="subjects abs">
  <thead><tr><th class="subject-col">Subjects</th><th>Primary</th><th>Secondary</th><th>GCSE</th><th>A- Level</th><th>University</th><th>Adult Learing</th></tr></thead>
  <tbody>
    <tr class="first"><td><span class="subj chem"><svg width="14" height="16" viewBox="0 0 14 16"><path d="M5 1h4M6 1v5L2 14h10L8 6V1" fill="none" stroke="#fff" stroke-width="1.5"/></svg>CHEMISTRY</span></td><td class="price-chem">£20</td><td></td><td class="price-chem">£25</td><td class="price-chem">£30</td><td></td><td></td></tr>
    <tr class="last"><td><span class="subj bio-s"><svg width="14" height="16" viewBox="0 0 14 16"><path d="M2 15h10M7 15V11M5 2l4 7" fill="none" stroke="#fff" stroke-width="1.5"/></svg>BIOLOGY</span></td><td class="price-bio">£20</td><td></td><td class="price-bio">£25</td><td class="price-bio">£30</td><td></td><td></td></tr>
  </tbody>
</table>

<!-- schedule -->
<h2 class="section-title abs" style="left:106px;top:1288px"><span class="hl">Available</span> Schedule</h2>
<div class="rule abs" style="left:106px;top:1356px;width:988px"></div>
<div class="month-nav abs">
  <span class="month-arrow" style="border-right:9px solid var(--coral)"></span>
  <span class="month">DECEMBER</span>
  <span class="month-arrow" style="border-left:9px solid var(--coral)"></span>
</div>
<div class="weekdays abs"><span>Su</span><span>Mo</span><span>Tu</span><span>We</span><span>Th</span><span>Fr</span><span>Sa</span></div>
<div class="calendar abs">
  <div></div><div></div><div></div><div></div><div>1</div><div>2</div><div class="taken">3</div>
  <div class="na">4</div><div>5</div><div>6</div><div>7</div><div class="taken">8</div><div>9</div><div>10</div>
  <div>11</div><div>12</div><div class="taken">13</div><div>14</div><div>15</div><div>16</div><div class="reserved">17</div>
  <div>18</div><div>19</div><div>20</div><div>21</div><div>22</div><div class="taken">23</div><div>24</div>
  <div class="holiday">25</div><div>26</div><div>27</div><div>28</div><div>29</div><div>30</div><div class="holiday">31</div>
</div>
<div class="legend abs">
  <span style="--c:var(--coral)">TAKEN</span><span style="--c:var(--amber)">RESERVED</span><span style="--c:var(--olive)">HOLIDAY</span><span style="--c:var(--blue)">NOT AVAILABLE</span>
</div>
<div class="btn btn-primary abs">Set an Appointment</div>
<div class="or abs">or</div>
<div class="btn btn-outline abs">Reserve a Date</div>

<!-- reviews -->
<section class="band-grey abs" style="top:1956px;height:670px"></section>
<h2 class="section-title abs" style="left:104px;top:2002px">Reviews</h2>
<div class="action-btn abs" style="left:517px;top:2011px"><svg width="18" height="16" viewBox="0 0 18 16"><ellipse cx="9" cy="7" rx="8" ry="6" fill="#fff"/><path d="M4 11l-1 4 5-3z" fill="#fff"/></svg></div>
<div class="rule abs" style="left:104px;top:2070px;width:447px"></div>
<p class="review-summary abs">2 reviews with an average rating of 4.0</p>

<article class="review abs" style="top:2141px">
  <div class="avatar"></div>
  <h3><span><span class="first">John</span> Doe</span><span style="color:#f68b1f"><svg class="star"><use href="#star"/></svg><svg class="star"><use href="#star"/></svg><svg class="star"><use href="#star"/></svg><svg class="star"><use href="#star"/></svg><svg class="star" style="color:#ccc"><use href="#star"/></svg></span></h3>
  <p>Lorem ipsum dolor sit amet, consectetur adipiscing elit, sed do eiusmod tempor incid­idunt ut labore et dolore magna aliqua.</p>
  <time>3 days ago</time>
</article>
<article class="review abs" style="top:2351px">
  <div class="avatar"></div>
  <h3><span><span class="first">Jane</span> Doe</span><span style="color:#f68b1f"><svg class="star"><use href="#star"/></svg><svg class="star"><use href="#star"/></svg><svg class="star"><use href="#star"/></svg><svg class="star"><use href="#star"/></svg><svg class="star" style="color:#ccc"><use href="#star"/></svg></span></h3>
  <p>Lorem ipsum dolor sit amet, consectetur adipiscing elit, sed do eiusmod tempor incid­idunt ut labore et dolore magna aliqua.</p>
  <time>3 days ago</time>
</article>

<div class="video abs">
  <div class="screen">
    <span class="name">LendYourLessons</span>
    <div class="bar"></div>
    <svg class="controls" viewBox="0 0 432 14" preserveAspectRatio="none"><path d="M2 1l10 6-10 6z" fill="#fff"/><rect x="398" y="3" width="10" height="8" fill="none" stroke="#fff" stroke-width="1.5"/><path d="M416 1h5M416 1v5M430 13h-5M430 13v-5" stroke="#fff" stroke-width="1.5" fill="none"/></svg>
  </div>
</div>

<footer class="site-footer abs">Copyright © 2016 LendYourLessons. Use of this website constitutes acceptance of our User Agreement and Privacy Policy.</footer>
</body>
</html>
```